Real Estate Sign to Help Modernize and Make it POP!

Design a sign style that would be good for marketing the sale or lease of properties. This will be 3 ' x 4' when printed and needs to look professional, modern, and catchy. It should us the company name, logo, and phone number at a minimum. Keep with the color scheme but open to varieties.

It will be printed and put in a large wooden frame as shown in one of the pictures.

Target Market(s)

Buyers and Tenants

Industry/Entity Type

Real Estate

Requirements
Must have
• company name, logo, and phone number
same color scheme as sign and website
Nice to have
• My Name, "Marlow Tefkin, CCIM"
Company Website
Ability to have an easy change from FOR SALE to FOR LEASE or FOR SALE/LEASE when I need to move this sign to a new property
An ability to have reflective colors printed on the contrast for cars to see at night
Should not have
• "Property Managed by"

```html
<!DOCTYPE html>
<html lang="en">
<head>
<meta charset="utf-8">
<title>Northway Crest Realty – For Sale Sign</title>
<link href="https://fonts.googleapis.com/css2?family=Oswald:wght@700&family=Montserrat:wght@500;600;800&family=Exo+2:wght@800&display=swap" rel="stylesheet">
<style>
  :root {
    --backdrop: #484546;
    --green-deep: #2e4a45;
    --green-light: #56786f;
    --green-text: #4f6961;
    --frame-line: #34504a;
    --white: #ffffff;
    --ink: #161616;
  }
  html, body {
    margin: 0;
    padding: 0;
    width: 1200px;
    height: 1200px;
    overflow: hidden;
    background: var(--backdrop);
  }
  .sign { display: block; width: 1200px; height: 1200px; }
  .brand-name { font-family: "Montserrat", sans-serif; font-weight: 500; fill: var(--white); }
  .headline { font-family: "Oswald", sans-serif; font-weight: 700; fill: var(--white); }
  .agent-name { font-family: "Exo 2", sans-serif; font-weight: 800; fill: var(--green-text); }
  .phone-number { font-family: "Montserrat", sans-serif; font-weight: 800; fill: var(--ink); }
  .website { font-family: "Montserrat", sans-serif; font-weight: 600; fill: var(--ink); }
  .contact-frame { fill: none; stroke: var(--frame-line); stroke-width: 2; }
  .phone-icon { fill: var(--ink); }
  .phone-waves { fill: none; stroke: var(--ink); stroke-width: 3; stroke-linecap: round; }
</style>
</head>
<body>
<svg class="sign" viewBox="0 0 1200 1200" xmlns="http://www.w3.org/2000/svg">
  <defs>
    <radialGradient id="bandGlow" cx="0.5" cy="0.25" r="0.65">
      <stop offset="0" stop-color="#56786f"/>
      <stop offset="1" stop-color="#2e4a45"/>
    </radialGradient>
    <clipPath id="bandClip">
      <rect x="50" y="188" width="1103" height="464"/>
    </clipPath>
  </defs>

  <!-- sign panel -->
  <rect class="sign-body" x="50" y="188" width="1103" height="826" fill="#ffffff"/>
  <rect class="header-band" x="50" y="188" width="1103" height="466" fill="url(#bandGlow)"/>

  <!-- brand -->
  <g class="brand">
    <circle cx="312" cy="313" r="70" fill="#ffffff"/>
    <text class="brand-name" x="402" y="346" font-size="80" textLength="553" lengthAdjust="spacingAndGlyphs">NORTHWAY</text>
    <text class="brand-name" x="678" y="390" font-size="28" text-anchor="middle" textLength="300" lengthAdjust="spacing">CREST REALTY</text>
  </g>

  <!-- status headline -->
  <g clip-path="url(#bandClip)">
    <text class="headline" x="200" y="706" font-size="316" textLength="798" lengthAdjust="spacingAndGlyphs">FOR SALE</text>
  </g>

  <!-- contact block -->
  <path class="contact-frame" d="M185 735 H118 V980 H1082 V735 H1015"/>
  <text class="agent-name" x="205" y="763" font-size="62" textLength="792" lengthAdjust="spacingAndGlyphs">MARLOW TEFKIN,<tspan font-size="38" dx="8">CCIM</tspan></text>

  <g class="phone-icon-group">
    <path class="phone-icon" d="M162 820 c-8 6 -10 20 -2 36 c10 20 24 34 42 42 c10 4 16 2 20 -4 l4 -6 c2 -3 1 -6 -2 -8 l-14 -9 c-3 -2 -6 -1 -8 1 l-5 5 c-10 -5 -20 -15 -25 -25 l5 -5 c2 -2 3 -5 1 -8 l-9 -15 c-2 -3 -5 -4 -7 -4 z"/>
    <path class="phone-waves" d="M190 832 a12 12 0 0 1 12 12"/>
    <path class="phone-waves" d="M192 820 a24 24 0 0 1 22 22"/>
    <path class="phone-waves" d="M194 808 a36 36 0 0 1 32 32"/>
  </g>
  <text class="phone-number" x="231" y="888" font-size="108" textLength="812" lengthAdjust="spacingAndGlyphs">555-270-4816</text>

  <text class="website" x="608" y="952" text-anchor="middle" font-size="40" textLength="734" lengthAdjust="spacingAndGlyphs">NORTHWAYCRESTREALTY.COM</text>
</svg>
</body>
</html>
```